Haverill’s

I would like a high class looking card with my logo and contact details (as per uploaded) Elegant, professional and highest quality feel

The following text included …..
“All commercial and residential painting work, large or small. Highest quality finishes and service.”

Industry/Entity Type

Painting

Contact Information for Business Card

Name, phone number, address, email address, company logo

Requirements
Must have
• Double sided

```html
<!DOCTYPE html>
<html lang="en">
<head>
<meta charset="utf-8">
<title>Haverill’s Quality Painters — Business Card</title>
<link rel="stylesheet" href="https://fonts.googleapis.com/css2?family=Cinzel:wght@400;600&family=Lato:wght@400;700&family=EB+Garamond:wght@400&display=swap">
<style>
  :root {
    --stage: #2a2a2a;
    --paper: #ffffff;
    --ink-dark: #1b1b1b;
    --gold: #b07f3a;
    --silver: #c8c8c8;
    --silver-line: #8a8a8a;
  }
  * { box-sizing: border-box; margin: 0; padding: 0; }
  html, body { width: 1200px; height: 800px; overflow: hidden; }
  body {
    background: var(--stage);
    display: flex;
    align-items: center;
    justify-content: center;
    gap: 40px;
  }
  .card {
    position: relative;
    width: 540px;
    height: 310px;
    border-radius: 22px;
    overflow: hidden;
  }
  .card--front { background: var(--paper); color: var(--gold); }
  .card--back { background: var(--ink-dark); }

  /* Brand lockup */
  .brand {
    position: absolute;
    display: flex;
    align-items: center;
    gap: 18px;
  }
  .brand__words { display: flex; flex-direction: column; align-items: flex-start; }
  .brand__name {
    font-family: "Cinzel", serif;
    font-weight: 400;
    font-size: 46px;
    letter-spacing: 1px;
    line-height: 1;
  }
  .brand__tagline {
    display: flex;
    align-items: center;
    gap: 10px;
    margin-top: 8px;
    font-family: "Lato", sans-serif;
    font-size: 13px;
    letter-spacing: 1.5px;
    text-transform: uppercase;
  }
  .brand__tagline::before,
  .brand__tagline::after {
    content: "";
    width: 46px;
    height: 1px;
    background: currentColor;
    opacity: .7;
  }
  .brand__circle {
    width: 88px;
    height: 88px;
    border-radius: 50%;
    border: 1.5px solid currentColor;
    flex: none;
  }

  .card--front .brand { top: 46px; left: 40px; }

  /* Front: person + contact */
  .person {
    position: absolute;
    left: 40px;
    top: 190px;
  }
  .person__name {
    font-family: "Cinzel", serif;
    font-weight: 600;
    font-size: 24px;
    letter-spacing: .5px;
  }
  .person__role {
    font-family: "Lato", sans-serif;
    font-size: 15px;
    margin-top: 2px;
  }
  .divider {
    position: absolute;
    left: 278px;
    top: 178px;
    width: 1px;
    height: 96px;
    background: var(--gold);
  }
  .contact {
    position: absolute;
    left: 298px;
    top: 176px;
    list-style: none;
    font-family: "Lato", sans-serif;
    font-size: 13px;
    line-height: 1.35;
  }
  .contact__item { display: flex; gap: 8px; align-items: flex-start; margin-bottom: 4px; }
  .contact__item--phone { font-weight: 700; font-size: 15px; }
  .contact__icon { width: 12px; height: 12px; flex: none; margin-top: 3px; fill: var(--gold); }

  /* Back */
  .card--back .brand { top: 62px; left: 50%; transform: translateX(-50%); color: var(--silver); }
  .card--back .brand__name { font-size: 50px; }
  .card--back .brand__tagline::before,
  .card--back .brand__tagline::after { background: var(--silver-line); }
  .statement {
    position: absolute;
    left: 0; right: 0;
    bottom: 58px;
    text-align: center;
    font-family: "EB Garamond", serif;
    font-size: 17px;
    line-height: 1.3;
    color: var(--gold);
  }
</style>
</head>
<body>

  <section class="card card--front" aria-label="Business card front">
    <div class="brand">
      <div class="brand__words">
        <span class="brand__name">Haverill’s</span>
        <span class="brand__tagline">Quality Painters</span>
      </div>
      <span class="brand__circle" aria-hidden="true"></span>
    </div>

    <div class="person">
      <p class="person__name">Owen Haverill</p>
      <p class="person__role">Owner</p>
    </div>

    <span class="divider" aria-hidden="true"></span>

    <ul class="contact">
      <li class="contact__item">
        <svg class="contact__icon" viewBox="0 0 12 12" aria-hidden="true"><path d="M6 0a4 4 0 0 0-4 4c0 3 4 8 4 8s4-5 4-8a4 4 0 0 0-4-4zm0 5.5A1.5 1.5 0 1 1 6 2.5a1.5 1.5 0 0 1 0 3z"/></svg>
        <span>42 Kowhai Terrace<br>Tawera Bay, 3590</span>
      </li>
      <li class="contact__item contact__item--phone">
        <svg class="contact__icon" viewBox="0 0 12 12" aria-hidden="true"><path d="M2.4 0.5l2 2.2-1 1.4a7 7 0 0 0 4.5 4.5l1.4-1 2.2 2-1.2 1.9C5 11.3.7 7 .5 1.7z"/></svg>
        <span>021 555 0147</span>
      </li>
      <li class="contact__item">
        <svg class="contact__icon" viewBox="0 0 12 12" aria-hidden="true"><path d="M0 2h12v8H0zM.8 2.6 6 6.6l5.2-4z" fill-rule="evenodd"/></svg>
        <span>owen@haverillpainters.example</span>
      </li>
    </ul>
  </section>

  <section class="card card--back" aria-label="Business card back">
    <div class="brand">
      <div class="brand__words">
        <span class="brand__name">Haverill’s</span>
        <span class="brand__tagline">Quality Painters</span>
      </div>
      <span class="brand__circle" aria-hidden="true"></span>
    </div>
    <p class="statement">All commercial and residential painting work,<br>large or small. Highest quality finishes and service.</p>
  </section>

</body>
</html>
```